Looking for a creative label design for our retail coffee bags

We are a coffee manufacturer (coffee roaster) looking to re-brand our retail label for our coffee bags. Our main coffee blend that we sell is our Harborline Velvet Blend. You can use this name when creating the label. We are going for a look that represents our company as a coffee roaster. Please reference our website (www.brindlemugworks.com) and our Facebook page to learn more about our company and to give you more inspiration on creating this design.

Target Market(s)

Retail customers/grocery stores

Industry/Entity Type

Manufacturer

Requirements
Must have
• The size of the label has to be 3" width x 4" height

Logo must be Black
Nice to have
• We currently incorporate a color on our labels for each blend. For example, Harborline Velvet Blend (royal blue), Decaffeinated Blend (red), Breakfast Blend (green), Flavored coffees (gold).

Rustic/vintage style

```html
<!DOCTYPE html>
<html lang="en">
<head>
<meta charset="utf-8">
<title>Brindle Mugworks – Harborline Velvet Blend Label</title>
<link rel="stylesheet" href="https://fonts.googleapis.com/css2?family=Barlow:wght@500;600&family=Barlow+Condensed:wght@400;700;800&display=swap">
<style>
  :root {
    --canvas: #ffffff;
    --roast-dark: #1c1c1c;
    --roast-mid: #4a4a4a;
    --roast-light: #7a7a7a;
    --seal: #f7f7f5;
    --ink: #1a1a1a;
    --blend-red: #c21f30;
    --label-text: #ffffff;
  }
  * { margin: 0; padding: 0; box-sizing: border-box; }
  html, body {
    width: 1200px; height: 950px; overflow: hidden;
    background: var(--canvas);
  }
  .coffee-label {
    position: absolute;
    left: 292px; top: 66px;
    width: 605px; height: 806px;
    overflow: hidden;
    color: var(--label-text);
    font-family: "Barlow", sans-serif;
  }
  .roaster-photo {
    position: absolute; inset: 0;
    background:
      radial-gradient(ellipse at 80% 35%, var(--roast-light) 0%, transparent 45%),
      radial-gradient(ellipse at 15% 30%, var(--roast-mid) 0%, transparent 40%),
      radial-gradient(ellipse at 55% 75%, var(--roast-mid) 0%, transparent 55%),
      var(--roast-dark);
  }
  .brand-seal {
    position: absolute;
    left: 96px; top: 114px;
    width: 404px; height: 404px;
    border-radius: 50%;
    background: var(--seal);
    display: flex; flex-direction: column;
    align-items: center; justify-content: center;
    color: var(--ink);
  }
  .brand-name {
    font-family: "Barlow Condensed", sans-serif;
    font-weight: 800;
    font-size: 74px;
    line-height: 0.95;
    text-transform: uppercase;
    text-align: center;
    letter-spacing: 1px;
  }
  .brand-tagline {
    margin-top: 26px;
    font-family: "Barlow Condensed", sans-serif;
    font-weight: 700;
    font-size: 13px;
    letter-spacing: 1.5px;
    text-transform: uppercase;
  }
  .blend-band {
    position: absolute;
    left: 106px; top: 582px;
    width: 402px; height: 44px;
    background: var(--blend-red);
    display: flex; align-items: center; justify-content: center;
    font-family: "Barlow Condensed", sans-serif;
    font-weight: 700;
    font-size: 24px;
    letter-spacing: 1.5px;
    text-transform: uppercase;
  }
  .blend-description {
    position: absolute;
    left: 0; right: 0; top: 640px;
    text-align: center;
    font-weight: 500;
    font-size: 15px;
    line-height: 22px;
    letter-spacing: -0.2px;
  }
  .spec-row {
    position: absolute;
    left: 0; right: 0; top: 710px;
    display: flex; justify-content: center; align-items: center;
  }
  .spec {
    width: 98px;
    text-align: center;
    font-family: "Barlow Condensed", sans-serif;
    font-weight: 400;
    font-size: 19px;
    line-height: 22px;
    text-transform: uppercase;
  }
  .spec-divider {
    width: 3px; height: 44px;
    background: var(--label-text);
  }
</style>
</head>
<body>
  <div class="coffee-label">
    <div class="roaster-photo" role="img" aria-label="Black and white photo of freshly roasted coffee beans tumbling in a roaster drum"></div>

    <div class="brand-seal">
      <div class="brand-name">Brindle<br>Mugworks</div>
      <div class="brand-tagline">Proudly roasted in Millbrook, OH since 1994.</div>
    </div>

    <div class="blend-band">Harborline Velvet Blend</div>

    <p class="blend-description">
      Made from the best Arabica beans South America has to offer, carefully<br>
      roasted to perfection.&nbsp; A distinctive rich aroma with a smooth undertones.
    </p>

    <div class="spec-row">
      <div class="spec">Whole<br>Bean</div>
      <div class="spec-divider"></div>
      <div class="spec">Dark<br>Roast</div>
      <div class="spec-divider"></div>
      <div class="spec">2LB<br>Net</div>
    </div>
  </div>
</body>
</html>
```